Business Card Design Project

Basic business card with minimal details. I just need company name, email & web address, telephone and my name.
I would like the back of the card to be grey with my logo & company name centred.

Target Market(s)

Architects
Builders
Property Developers

Industry/Entity Type

Business

Font styles to use
Sans Serif

Colors

Designer to choose colors to be used in the design.

Requirements
Must have
• Framewise Build
Marcus Helby - Director
M: 0427 593184
E: marcus@framewisebuild.com.au
W: www.framewisebuild.com.au
Should not have
• No other images or pictures

```html
<!DOCTYPE html>
<html lang="en">
<head>
<meta charset="utf-8">
<title>Framewise Build – Business Cards</title>
<link href="https://fonts.googleapis.com/css2?family=Open+Sans:ital,wght@0,400;1,400&family=Ubuntu:wght@500;700&display=swap" rel="stylesheet">
<style>
  :root {
    --crimson: #a8113a;
    --slate: #4b5e6d;
    --paper: #ffffff;
    --ink: #222222;
    --rule: #8a8f94;
    --backdrop: #d9dadc;
  }
  * { box-sizing: border-box; margin: 0; padding: 0; }
  html, body { width: 1200px; height: 1000px; overflow: hidden; }
  body {
    background: var(--backdrop);
    position: relative;
    font-family: "Open Sans", Arial, sans-serif;
  }
  .card {
    position: absolute;
    box-shadow: 0 4px 10px rgba(0,0,0,.35);
    overflow: hidden;
  }
  /* Front */
  .card-front {
    left: 320px; top: 50px; width: 560px; height: 300px;
    background: var(--paper);
  }
  .front-brand {
    position: absolute; right: 36px; top: 48px;
    display: flex; align-items: center; gap: 10px;
  }
  .brand-square {
    width: 26px; height: 26px;
    border: 3px solid var(--crimson);
  }
  .brand-name {
    font-family: "Ubuntu", Arial, sans-serif;
    font-weight: 500;
    color: var(--slate);
    letter-spacing: 1.5px;
    text-transform: uppercase;
  }
  .front-brand .brand-name { font-size: 19px; }
  .holder-name {
    position: absolute; left: 76px; top: 92px;
    font-family: "Ubuntu", Arial, sans-serif;
    font-weight: 700; font-size: 19px; letter-spacing: .8px;
    color: var(--crimson);
  }
  .holder-role {
    position: absolute; left: 72px; top: 117px;
    font-style: italic; font-size: 11px; color: var(--ink);
  }
  .header-rule {
    position: absolute; left: 136px; right: 40px; top: 126px;
    height: 1px; background: var(--rule);
  }
  .contact-list {
    position: absolute; left: 56px; top: 180px;
    list-style: none; font-size: 13px; color: var(--ink);
  }
  .contact-list li {
    display: flex; align-items: center; gap: 8px; height: 22px;
  }
  .contact-list svg { width: 12px; height: 12px; fill: var(--crimson); }
  .front-bands { position: absolute; left: 0; bottom: 0; width: 560px; height: 26px; }

  /* Backs */
  .card-back {
    width: 480px; height: 270px;
    display: flex; flex-direction: column; align-items: center; justify-content: center; gap: 22px;
  }
  .card-back .brand-square { width: 70px; height: 70px; border-width: 5px; transform: rotate(45deg); }
  .card-back .brand-name { font-size: 32px; letter-spacing: 2px; }
  .back-slate { left: 80px; top: 400px; background: var(--slate); }
  .back-slate .brand-name { color: var(--paper); }
  .back-paper { left: 640px; top: 400px; background: var(--paper); }
  .back-mono { left: 360px; top: 705px; background: var(--slate); }
  .back-mono .brand-square { border-color: var(--paper); }
  .back-mono .brand-name { color: var(--paper); }
</style>
</head>
<body>

<section class="card card-front" aria-label="Business card front">
  <div class="front-brand">
    <span class="brand-square"></span>
    <span class="brand-name">Framewise Build</span>
  </div>
  <h1 class="holder-name">Marcus Helby</h1>
  <p class="holder-role">Director</p>
  <div class="header-rule"></div>
  <ul class="contact-list">
    <li><svg viewBox="0 0 12 12" aria-hidden="true"><path d="M3 0h6a1 1 0 0 1 1 1v10a1 1 0 0 1-1 1H3a1 1 0 0 1-1-1V1a1 1 0 0 1 1-1zm0 2v7h6V2z"/></svg>0427 593184</li>
    <li><svg viewBox="0 0 12 12" aria-hidden="true"><path d="M0 2h12v8H0zM1 3l5 4 5-4v-.2H1z"/></svg>marcus@framewisebuild.com.au</li>
    <li><svg viewBox="0 0 12 12" aria-hidden="true"><path d="M6 0a6 6 0 1 0 0 12A6 6 0 0 0 6 0zm0 1.2c.6.7 1 1.9 1.2 3.3H4.8C5 3.1 5.4 1.9 6 1.2zM1.3 5.5h2.5c0 .4 0 .7 0 1H1.3a4.8 4.8 0 0 1 0-1zm3.5 0h2.4v1H4.8zm3.4 0h2.5a4.8 4.8 0 0 1 0 1H8.2zM4.8 7.5h2.4C7 8.9 6.6 10.1 6 10.8c-.6-.7-1-1.9-1.2-3.3z"/></svg>www.framewisebuild.com.au</li>
  </ul>
  <svg class="front-bands" viewBox="0 0 560 26" aria-hidden="true">
    <polygon points="0,8 346,8 342,26 0,26" fill="var(--crimson)"/>
    <path d="M352,26 L358,8 Q360,0 372,0 L560,0 L560,26 Z" fill="var(--slate)"/>
  </svg>
</section>

<section class="card card-back back-slate" aria-label="Business card back, grey">
  <span class="brand-square"></span>
  <span class="brand-name">Framewise Build</span>
</section>

<section class="card card-back back-paper" aria-label="Business card back, white">
  <span class="brand-square"></span>
  <span class="brand-name">Framewise Build</span>
</section>

<section class="card card-back back-mono" aria-label="Business card back, grey with white mark">
  <span class="brand-square"></span>
  <span class="brand-name">Framewise Build</span>
</section>

</body>
</html>
```